Website design for management consulting firm

We need a web design for a new consulting company based in Boston, MA called "Marlow Ridge Consulting." This webpage will be simple home page, with a "contact us" page, that describes the services of the consulting firm. The company provides strategic planning, business assessment, process re-designs, and other management consulting functions. I would like the website to look high-tech. A logo was already created via Artfolk Hub.

Target Market(s)

Other business owners across a wide spectrum of industries - from IT to retail.

Industry/Entity Type

It Company

Number of Pages Required

3 page

Colors
0455a3
ffffff

Requirements
Must have
• Front page that provides generic text / overview of the firm. A "services" tab that describes consulting services. A "contact us" tab that provides either a form to contact us or just the contact email address of the company. info@marlowridgeconsulting.example

```html
<!DOCTYPE html>
<html lang="en">
<head>
<meta charset="utf-8">
<title>Marlow Ridge Consulting</title>
<link rel="stylesheet" href="https://fonts.googleapis.com/css2?family=Open+Sans:ital,wght@0,400;0,600;0,700;1,400&display=swap">
<style>
:root{
  --brand:#0b5f88;
  --brand-dark:#0a3b58;
  --accent-red:#b10f13;
  --title-blue:#1b6390;
  --text:#555;
  --white:#fff;
  --dot:#4a4a4a;
}
*{margin:0;padding:0;box-sizing:border-box}
html,body{width:1015px;height:1200px;overflow:hidden;background:var(--white)}
body{position:relative;font-family:"Open Sans",Arial,sans-serif;color:var(--text)}

.hero{position:absolute;left:0;top:0;width:1015px;height:507px;
  background:linear-gradient(100deg,#8a8f95 0%,#b9a48a 22%,#d8cbb8 38%,#6b6e73 55%,#3c3f45 70%,#58524c 85%,#8d8e90 100%)}
.hero::after{content:"";position:absolute;inset:0;background:rgba(20,25,35,.38)}

.site-header{position:absolute;left:158px;top:0;width:698px;height:78px;background:var(--white);z-index:2}
.brand{position:absolute;left:20px;top:21px;display:flex;align-items:center;gap:10px}
.brand-mark{width:34px;height:34px;background:var(--brand)}
.brand-name{font-size:17px;font-weight:700;color:#1d1d1d;letter-spacing:-.3px}
.main-nav{position:absolute;left:312px;top:30px;display:flex;gap:14px;font-size:11px}
.main-nav a{color:#444;text-decoration:none}
.main-nav a.active{color:var(--title-blue)}
.header-search{position:absolute;left:656px;top:28px}

.hero-content{position:absolute;left:0;top:196px;width:1015px;text-align:center;color:var(--white);z-index:2}
.hero-title{font-size:29px;font-weight:600;line-height:40px}
.hero-tagline{font-size:12.5px;font-style:italic;margin-top:4px}
.hero-text{width:550px;margin:11px auto 0;font-size:13px;line-height:16px}
.btn-read{display:block;width:161px;height:38px;margin:33px auto 0;background:var(--white);color:#222;
  font-size:14.5px;font-weight:700;line-height:38px;text-decoration:none}

.services-head{position:absolute;left:0;top:553px;width:1015px;text-align:center}
.services-title{font-size:21.5px;font-weight:400;color:var(--title-blue)}
.services-sub{font-size:13.5px;margin-top:4px}

.service{position:absolute;top:634px;width:231px}
.service-photo{position:relative;height:184px;border:1px solid #ccc;overflow:hidden}
.service-label{position:absolute;left:0;bottom:0;height:22px;width:100%;
  background:linear-gradient(100deg,var(--accent-red) 0%,var(--accent-red) 84%,rgba(40,60,120,.7) 84.5%,rgba(40,60,120,.7) 100%);
  color:var(--white);font-size:14px;line-height:22px;padding-left:18px}
.service-text{font-size:12px;line-height:15.5px;margin-top:10px;color:#555}

.slider-dots{position:absolute;left:464px;top:906px;display:flex;gap:8px}
.slider-dots span{width:11px;height:11px;border-radius:50%;background:var(--dot)}
.slider-dots span.open{background:var(--white);border:1px solid var(--dot)}

.site-footer{position:absolute;left:0;top:972px;width:1015px;height:188px;background:var(--brand);color:var(--white)}
.footer-col{position:absolute;top:35px}
.footer-col h3{font-size:13px;font-weight:700;margin-bottom:10px}
.footer-col p,.footer-col li{font-size:9px;line-height:15px;list-style:none}
.footer-col p{line-height:11.5px}
.footer-search{width:114px;height:18px;background:var(--white);position:relative;color:#666;font-size:9px;line-height:18px;padding-left:7px}
.footer-search svg{position:absolute;right:5px;top:3px}
.social{display:flex;gap:8px;margin-top:2px}
.social span{width:11px;height:11px;border-radius:50%;background:var(--white)}
.bottom-bar{position:absolute;left:0;top:1160px;width:1015px;height:40px;background:var(--brand-dark);color:var(--white);font-size:8px}
.bottom-bar .copy{position:absolute;left:158px;top:15px}
.bottom-bar .rights{position:absolute;right:159px;top:15px}
</style>
</head>
<body>

<section class="hero" role="img" aria-label="Photo of business people in a meeting around a table"></section>

<header class="site-header">
  <div class="brand"><span class="brand-mark"></span><span class="brand-name">Marlow Ridge Consulting</span></div>
  <nav class="main-nav">
    <a class="active" href="#">Home</a><a href="#">About us</a><a href="#">Our work</a><a href="#">Careers</a><a href="#">Blog</a><a href="#">Contect us</a>
  </nav>
  <svg class="header-search" width="20" height="20" viewBox="0 0 20 20"><circle cx="8" cy="8" r="6" fill="none" stroke="#222" stroke-width="2.6"/><line x1="12.5" y1="12.5" x2="18" y2="18" stroke="#222" stroke-width="3" stroke-linecap="round"/></svg>
</header>

<div class="hero-content">
  <h1 class="hero-title">Lorem Ipsum is simply dummy text</h1>
  <p class="hero-tagline">Lorem Ipsum is simply dummy text of the printing and typesetting industry.</p>
  <p class="hero-text">Lorem Ipsum is simply dummy text of the printing and typesetting industry. Lorem Ipsum has been the industry's standard dummy text ever since the 1500s, when an unknown printer took a galley of type and scrambled it to make .</p>
  <a class="btn-read" href="#">Read more</a>
</div>

<div class="services-head">
  <h2 class="services-title">The company provides</h2>
  <p class="services-sub">Lorem Ipsum is simply dummy text of the printing and typesetting industry.</p>
</div>

<article class="service" style="left:158px">
  <div class="service-photo" role="img" aria-label="Photo of a consultant meeting with two clients" style="background:linear-gradient(120deg,#9aa3a8,#6b5a48 55%,#c9c2b8)">
    <div class="service-label">Strategic Planning</div>
  </div>
  <p class="service-text">Lorem Ipsum is simply dummy text of the printing and typesetting industry. Lorem Ipsum has been the industry's.</p>
</article>
<article class="service" style="left:392px">
  <div class="service-photo" role="img" aria-label="Photo of two colleagues reviewing documents" style="background:linear-gradient(120deg,#dfe3e6,#b9bcc0 50%,#e8e4dc)">
    <div class="service-label">Business assessment</div>
  </div>
  <p class="service-text">Lorem Ipsum is simply dummy text of the printing and typesetting industry. Lorem Ipsum has been the industry's.</p>
</article>
<article class="service" style="left:625px">
  <div class="service-photo" role="img" aria-label="Photo of a desk with a computer monitor and office supplies" style="background:linear-gradient(130deg,#6f8f4a,#a57a4f 45%,#5f8fa8 75%,#3a6f9a)">
    <div class="service-label">Process re-designs</div>
  </div>
  <p class="service-text">Lorem Ipsum is simply dummy text of the printing and typesetting industry. Lorem Ipsum has been the industry's.</p>
</article>

<div class="slider-dots"><span></span><span class="open"></span><span></span><span></span><span></span></div>

<footer class="site-footer">
  <div class="footer-col" style="left:159px;width:150px">
    <h3>Our Company</h3>
    <p>Lorem Ipsum is simply dummy text of the printing and typesetting industry. Lorem Ipsum has been the industry's standard dummy text ever since the 1500s,</p>
  </div>
  <div class="footer-col" style="left:348px">
    <h3>Our Link</h3>
    <ul><li>Home</li><li>About us</li><li>Our work</li><li>Careers</li><li>Blog</li><li>Contect us</li></ul>
  </div>
  <div class="footer-col" style="left:450px">
    <h3>The Company Provide</h3>
    <ul><li>Stratergic planing</li><li>Business assessment</li><li>Process re-designs</li><li>Other</li></ul>
  </div>
  <div class="footer-col" style="left:630px">
    <h3>Search</h3>
    <div class="footer-search">Type here..
      <svg width="13" height="13" viewBox="0 0 20 20"><circle cx="8" cy="8" r="6" fill="none" stroke="#222" stroke-width="2.6"/><line x1="12.5" y1="12.5" x2="18" y2="18" stroke="#222" stroke-width="3" stroke-linecap="round"/></svg>
    </div>
  </div>
  <div class="footer-col" style="left:795px">
    <h3>Follow us</h3>
    <div class="social"><span></span><span></span><span></span></div>
  </div>
</footer>

<div class="bottom-bar">
  <span class="copy">Copyright © 2015 Marlow Ridge Consulting.</span>
  <span class="rights">All reserved.</span>
</div>

</body>
</html>
```